Reef Lantern Tropical Fish Startup Design

I need professional business cards and social media profiles for our tropical fish shop.

Target Market(s)

Tropical fish enthusiasts

Industry/Entity Type

Tropical Fish

Font styles to use
Sans Serif
Script
Other font styles liked:
• Comforta

Colors
0054AA
0677BA
7BADD7
CADEEF
E8F1F8
0094D4
00A9DD
6FCCEA
C7EBF8
E9F6FB
00AB8E
00BBA5
67D7C9
C6EFE9
E9F9F6

Requirements
Must have
• fish, oceanic colors
Nice to have
• Lines, boxes, anything that groups the title to stand out
Should not have
• Any punctuations

```html
<!DOCTYPE html>
<html lang="en">
<head>
<meta charset="utf-8">
<title>Reef Lantern Stationery</title>
<link rel="stylesheet" href="https://fonts.googleapis.com/css2?family=Open+Sans:wght@400;600;700&family=Roboto:wght@400;500&display=swap">
<style>
:root{
  --teal:#2aa78a;
  --teal-soft:#d6ece6;
  --blue:#2f68a8;
  --ink:#4a4a4a;
  --paper:#f5f5f5;
  --desk:#e8e8e8;
  --white:#ffffff;
}
*{margin:0;padding:0;box-sizing:border-box}
html,body{width:1200px;height:795px;overflow:hidden}
body{background:var(--desk);position:relative;font-family:"Open Sans",sans-serif;color:var(--ink)}
.piece{position:absolute;overflow:hidden}
.wordmark{font-family:"Open Sans",sans-serif;font-weight:700;color:var(--teal);white-space:nowrap;letter-spacing:-.01em;line-height:1}
.wordmark.on-teal{color:var(--white)}
.band{position:absolute;left:0;right:0;bottom:0;display:block}

/* letterhead */
.letterhead{left:292px;top:99px;width:293px;height:414px;background:var(--paper)}
.letterhead .wordmark{position:absolute;left:31px;top:34px;font-size:13px}
.lh-address{position:absolute;left:126px;top:31px;font-family:"Roboto",sans-serif;font-size:6.4px;line-height:8.2px;color:var(--ink)}
.lh-address .company{color:var(--teal);font-family:"Open Sans",sans-serif;font-weight:600}
.lh-contact{position:absolute;left:188px;top:31px;font-family:"Roboto",sans-serif;font-size:6.4px;line-height:8.2px;color:var(--ink);list-style:none}
.lh-contact li{display:flex;align-items:center;gap:2.5px}
.lh-contact svg{width:5px;height:5px;fill:var(--teal)}
.letter-body{position:absolute;left:31px;top:106px;width:231px;font-size:5.2px;line-height:7.7px;color:var(--ink)}
.letter-body p{margin-bottom:7.6px;text-align:justify}
.signature-area{position:absolute;left:31px;top:306px;width:34px;height:32px;background:#ececec;border-radius:3px}

/* folder */
.folder{left:636px;top:80px;width:347px;height:437px;background:var(--teal)}
.folder .spine{position:absolute;top:0;bottom:0;width:1px;background:rgba(0,0,0,.12)}
.folder .wordmark{position:absolute;left:0;right:0;top:205px;text-align:center;font-size:36px}
.folder .web{position:absolute;left:0;right:0;top:398px;text-align:center;font-size:9.5px;color:var(--white)}
.folder .web b{font-weight:700}

/* business cards */
.card{left:186px;width:132px;height:75px}
.card-front{top:550px;background:var(--teal)}
.card-front .wordmark{position:absolute;left:0;right:0;top:26px;text-align:center;font-size:15px}
.card-front .handle{position:absolute;left:0;right:0;top:62px;text-align:center;font-size:4.2px;color:var(--white)}
.card-back{top:646px;background:var(--paper)}
.card-back .wordmark{position:absolute;left:10px;top:14px;font-size:8px}
.card-back .decor{position:absolute;right:0;top:28px;width:52px;height:40px;background:linear-gradient(120deg,rgba(42,167,138,.12),rgba(42,167,138,.04));border-radius:20px 0 0 14px}
.person{position:absolute;right:10px;top:17px;text-align:right;line-height:5px}
.person .name{font-size:4.8px;font-weight:700;color:var(--teal);text-transform:uppercase}
.person .role{font-size:3.8px;color:var(--blue)}
.card-details{position:absolute;left:10px;top:38px;font-size:3.8px;line-height:4.8px;color:var(--ink);list-style:none}
.card-details li{display:flex;align-items:center;gap:1.5px}
.card-details svg{width:3.6px;height:3.6px;fill:var(--teal)}
.card-details .gap{margin-top:2px}

/* envelopes */
.envelope{top:561px;width:328px;height:157px;background:var(--paper)}
.envelope-front{left:353px}
.envelope-front .decor{position:absolute;left:164px;top:8px;width:162px;height:140px;background:radial-gradient(ellipse at 55% 45%,rgba(42,167,138,.13),rgba(42,167,138,0) 70%)}
.envelope-front .wordmark{position:absolute;left:23px;top:28px;font-size:15px}
.env-address{position:absolute;left:23px;top:108px;font-family:"Roboto",sans-serif;font-size:7.2px;line-height:8.8px;color:var(--ink)}
.env-address .company{color:var(--teal);font-family:"Open Sans",sans-serif;font-weight:600}
.envelope-back{left:713px}
.envelope-back .flap{position:absolute;left:0;top:0}
.envelope-back .wordmark{position:absolute;left:0;right:0;top:23px;text-align:center;font-size:13px}
</style>
</head>
<body>

<section class="piece letterhead" aria-label="Letterhead">
  <div class="wordmark">Reef Lantern</div>
  <address class="lh-address">
    <span class="company">Reef Lantern Inc.</span><br>p.o box 41207<br>harbor city, nv 89022
  </address>
  <ul class="lh-contact">
    <li><svg viewBox="0 0 10 10"><path d="M2 0l2 2.4-1.2 1.4c.6 1.4 1.8 2.6 3.2 3.2L7.4 5.8 10 8 8.4 10C4 9.6.4 6 0 1.6z"/></svg>(555) 014-2290</li>
    <li><svg viewBox="0 0 10 10"><path d="M0 2h10v6H0zM.6 2.4L5 5.6l4.4-3.2"/></svg>hello@reeflantern.com</li>
    <li><svg viewBox="0 0 10 10"><path d="M5 0a5 5 0 100 10A5 5 0 005 0zm0 1.2a3.8 3.8 0 110 7.6 3.8 3.8 0 010-7.6z"/></svg>www.reeflantern.com</li>
  </ul>
  <div class="letter-body">
    <p>Dear customer,</p>
    <p>Lorem ipsum dolor sit amet, consectetur adipisicing elit, sed do eiusmod tempor incididunt ut labore et dolore magna aliqua. Ut enim ad minim veniam, quis nostrud exercitation ullamco laboris nisi ut aliquip ex ea commodo consequat. Duis aute irure dolor in reprehenderit in voluptate velit esse cillum dolore eu fugiat nulla pariatur. Excepteur sint occaecat cupidatat non proident, sunt in culpa qui officia deserunt mollit anim id est laborum.</p>
    <p>Lorem ipsum dolor sit amet, consectetur adipisicing elit, sed do eiusmod tempor incididunt ut labore et dolore magna aliqua. Ut enim ad minim veniam, quis nostrud exercitation ullamco laboris nisi ut aliquip ex ea commodo consequat. Duis aute irure dolor in reprehenderit in voluptate velit esse cillum dolore eu fugiat nulla pariatur. Excepteur sint occaecat cupidatat non proident, sunt in culpa qui officia deserunt mollit anim id est laborum.</p>
    <p>Lorem ipsum dolor sit amet, consectetur adipisicing elit, sed do eiusmod tempor incididunt ut labore et dolore magna aliqua. Ut enim ad minim veniam, quis nostrud exercitation ullamco laboris nisi ut aliquip ex ea commodo consequat. Duis aute irure dolor in reprehenderit in voluptate velit esse cillum dolore eu fugiat nulla pariatur. Excepteur sint occaecat cupidatat non proident, sunt in culpa qui officia deserunt mollit anim id est laborum.</p>
    <p>Lorem ipsum dolor sit amet, consectetur adipisicing elit, sed do eiusmod tempor incididunt ut labore et dolore magna aliqua. Ut enim ad minim veniam, quis nostrud exercitation ullamco laboris nisi ut aliquip ex ea commodo consequat. Duis aute irure dolor in reprehenderit.</p>
    <p>Yours Sincerely,</p>
  </div>
  <div class="signature-area" role="img" aria-label="Handwritten signature"></div>
  <svg class="band" width="293" height="7" viewBox="0 0 293 7" preserveAspectRatio="none">
    <rect width="293" height="7" fill="var(--teal)"/>
    <polygon points="0,0 95,0 89,7 0,7" fill="var(--blue)"/>
  </svg>
</section>

<section class="piece folder" aria-label="Presentation folder">
  <span class="spine" style="left:4px"></span>
  <span class="spine" style="left:10px"></span>
  <span class="spine" style="left:19px"></span>
  <div class="wordmark on-teal">Reef Lantern</div>
  <div class="web">www.<b>reeflantern</b>.com</div>
</section>

<section class="piece card card-front" aria-label="Business card front">
  <div class="wordmark on-teal">Reef Lantern</div>
  <div class="handle">@reeflantern</div>
</section>

<section class="piece card card-back" aria-label="Business card back">
  <div class="decor" role="img" aria-label="Faint tropical fish silhouette"></div>
  <div class="wordmark">Reef Lantern</div>
  <div class="person">
    <div class="name">Marlo Vance</div>
    <div class="role">Managing Director</div>
  </div>
  <ul class="card-details">
    <li>Reef Lantern Inc.</li>
    <li>P.O Box 41207</li>
    <li>Harbor City, NV 89022</li>
    <li class="gap"><svg viewBox="0 0 10 10"><path d="M2 0l2 2.4-1.2 1.4c.6 1.4 1.8 2.6 3.2 3.2L7.4 5.8 10 8 8.4 10C4 9.6.4 6 0 1.6z"/></svg>+15550138842</li>
    <li><svg viewBox="0 0 10 10"><path d="M0 2h10v6H0z"/></svg>hello@reeflantern.com</li>
    <li><svg viewBox="0 0 10 10"><path d="M5 0a5 5 0 100 10A5 5 0 005 0zm0 1.2a3.8 3.8 0 110 7.6 3.8 3.8 0 010-7.6z"/></svg>www.reeflantern.com</li>
  </ul>
  <svg class="band" width="132" height="3" viewBox="0 0 132 3" preserveAspectRatio="none">
    <rect width="132" height="3" fill="var(--teal)"/>
    <polygon points="0,0 68,0 65,3 0,3" fill="var(--blue)"/>
  </svg>
</section>

<section class="piece envelope envelope-front" aria-label="Envelope front">
  <div class="decor" role="img" aria-label="Faint tropical fish silhouette"></div>
  <div class="wordmark">Reef Lantern</div>
  <address class="env-address">
    <span class="company">Reef Lantern Inc.</span><br>p.o box 41207<br>harbor city, nv 89022
  </address>
  <svg class="band" width="328" height="8" viewBox="0 0 328 8" preserveAspectRatio="none">
    <rect width="328" height="8" fill="var(--teal)"/>
    <polygon points="0,0 98,0 105,8 0,8" fill="var(--blue)"/>
  </svg>
</section>

<section class="piece envelope envelope-back" aria-label="Envelope back">
  <svg class="flap" width="328" height="56" viewBox="0 0 328 56">
    <path d="M0 0H328L322 48Q321 55 314 55H14Q7 55 6 48Z" fill="var(--teal)"/>
  </svg>
  <div class="wordmark on-teal">Reef Lantern</div>
</section>

</body>
</html>
```